frozen yogurt & dessert bar need a franchise booklet

I need a franchise booklet , attached will be a sample of the franchise booklet( mesa crullo franchise info kit.pdf) which I need the project to look like. I will also a provide the text with the photos( in red color) that I expect to have with each phase (FRANCHISE BOOKLET TEXT.PDF). I have provided some new photos that you can use with the old ones ( earlier project).

Target Market(s)

food and beverage

Requirements
Must have
• should be an A4 PORTRAIT BOOKLET , PLEASE USE THE PHOTOS PROVIDED AND OTHER PHOTOS THAT HAVE BEEN USED IN THE PREVIOUS PROJECT.
Nice to have
• photos that would be used should have some element of our logo, for example if there is a photo of a store or a product out logo should be found on. there is a photo of a store in a mall that I need to remove the tavola bin from it and write FLOMBERAY instead while adding the wide logo. also I need to make the interior or blur so it doesn't seem as a pizza place.

```html
<!DOCTYPE html>
<html lang="en">
<head>
<meta charset="utf-8">
<title>FLOMBERAY Franchise Booklet – Pages 21–24</title>
<link href="https://fonts.googleapis.com/css2?family=Open+Sans:wght@400;600;700;800&display=swap" rel="stylesheet">
<style>
  :root {
    --red: #ec3c3a;
    --red-deep: #c8202a;
    --red-ribbon: #d9262c;
    --pink: #f3a3a0;
    --pink-soft: #f9cfcd;
    --ink: #1d1d1d;
    --white: #ffffff;
    --paper: #ffffff;
    --page-bg: #ffffff;
    --overlay: rgba(120, 120, 120, 0.72);
  }
  * { box-sizing: border-box; margin: 0; padding: 0; }
  html, body { width: 851px; height: 1200px; overflow: hidden; background: var(--page-bg); }
  body { font-family: "Open Sans", Arial, sans-serif; color: var(--ink); }
  .canvas { position: relative; width: 851px; height: 1200px; overflow: hidden; background: var(--page-bg); }

  .spread { position: absolute; left: 38px; width: 767px; height: 545px; box-shadow: 0 3px 10px rgba(0,0,0,0.25); overflow: hidden; }
  .spread--faq { top: 25px; }
  .spread--photo { top: 633px; }

  .page { position: absolute; top: 0; width: 383.5px; height: 545px; overflow: hidden; }
  .page--left { left: 0; }
  .page--right { left: 383.5px; }
  .page--white { background: var(--paper); }
  .page--red { background: var(--red); }

  .waves { position: absolute; left: 0; bottom: 0; width: 100%; height: 150px; }

  .ribbon { position: absolute; top: 46px; left: 0; width: 384px; height: 40px; }
  .ribbon svg { position: absolute; left: 0; top: 0; }
  .ribbon__title { position: absolute; top: 4px; white-space: nowrap; font-weight: 700; font-size: 14px; line-height: 20px; color: var(--white); text-transform: uppercase; }

  .page-tab { position: absolute; top: 142px; width: 17px; height: 120px; }
  .page-tab__num { position: absolute; top: 40px; width: 17px; text-align: center; font-size: 10px; line-height: 15px; color: var(--white); font-weight: 600; }
  .page--left .page-tab { left: 0; }
  .page--right .page-tab { right: 0; }

  .content { position: absolute; top: 94px; font-size: 7.1px; line-height: 11.6px; }
  .page--left .content { left: 45px; width: 296px; }
  .page--right .content { left: 46px; width: 308px; color: var(--white); }
  .faq { margin-bottom: 8px; }
  .faq__q { font-weight: 800; font-size: 8.2px; line-height: 12px; color: var(--red); text-transform: uppercase; margin-bottom: 1px; }
  .page--right .faq__q { color: var(--white); }
  .page--right .faq { margin-bottom: 18px; }
  .faq__a { text-align: justify; font-weight: 600; }

  .brand { position: absolute; display: flex; align-items: center; gap: 5px; }
  .brand__dot { width: 12px; height: 12px; border-radius: 50%; }
  .brand__name { font-weight: 800; font-size: 15px; letter-spacing: 0.3px; }
  .brand--red .brand__dot { background: var(--red); }
  .brand--red .brand__name { color: var(--red); }
  .brand--white .brand__dot { background: var(--white); }
  .brand--white .brand__name { color: var(--white); }

  .folio { position: absolute; bottom: 14px; font-size: 5.6px; font-weight: 700; text-transform: uppercase; color: var(--red); }
  .page--red .folio { color: var(--white); }

  .photo { position: absolute; inset: 0;
    background: linear-gradient(100deg, #b9b6b0 0%, #c4c0b8 40%, #cdc5b8 65%, #d9ccb9 100%);
  }
  .slogan-box { position: absolute; left: 59px; top: 72px; width: 281px; height: 277px; background: var(--overlay); color: var(--white); padding: 19px 12px; font-size: 7.6px; font-weight: 700; line-height: 11px; }
  .slogan-box .lead { margin-bottom: 19px; }
  .slogan-box .headline { margin-bottom: 30px; }
  .slogan-box .slogan { margin-bottom: 14px; }
  .photo-tab { position: absolute; top: 135px; width: 17px; height: 120px; }
  .photo-tab--left { left: 0; }
  .photo-tab--right { right: 0; }
</style>
</head>
<body>
<main class="canvas">

  <section class="spread spread--faq">
    <article class="page page--left page--white">
      <svg class="waves" viewBox="0 0 384 150" preserveAspectRatio="none" aria-hidden="true">
        <path d="M0 20 C80 60 160 40 230 70 C300 100 340 130 384 125 L384 150 L0 150 Z" fill="var(--pink-soft)"/>
        <path d="M0 35 C60 55 70 120 150 130 C230 140 300 110 384 120 L384 150 L0 150 Z" fill="var(--pink)"/>
      </svg>

      <div class="ribbon">
        <svg width="384" height="40" viewBox="0 0 384 40" aria-hidden="true">
          <rect x="0" y="0" width="384" height="27" fill="#f1f1f1"/>
          <polygon points="0,0 283,0 271,27 0,27" fill="var(--red)"/>
          <polygon points="258,27 271,27 265,36" fill="var(--red-deep)"/>
        </svg>
        <h2 class="ribbon__title" style="left:47px;">Frequently Asked Questions</h2>
      </div>

      <div class="page-tab">
        <svg width="17" height="120" viewBox="0 0 17 120" aria-hidden="true"><polygon points="0,0 17,18 17,102 0,120" fill="var(--red)"/></svg>
        <div class="page-tab__num">2<br>1</div>
      </div>

      <div class="content">
        <div class="faq">
          <h3 class="faq__q">What is the initial investment?</h3>
          <p class="faq__a">The initial investment includes the franchise fee, store design, store construction and training. Depending on the location and store size the cost may vary :<br>Kiosk $175,000 – 250,000 (plus applicable taxes)<br>Street front or Mega store $250,000 – $550,000 (plus applicable taxes)</p>
        </div>
        <div class="faq">
          <h3 class="faq__q">How can I finance my business?</h3>
          <p class="faq__a">One of the most common ways to finance your business is to use the Canadian small business loan which is provided by most major banks in Canada. The Canadian small business program loan provides loans that is associated with business assets (e.g.: equipment &amp; construction). Other lending programs are also available by financial groups and providers.</p>
        </div>
        <div class="faq">
          <h3 class="faq__q">Does FLOMBERAY help with location selection and the lease?</h3>
          <p class="faq__a">FLOMBERAY will assist in securing a location and deal with landlords to ensure that a franchisee gets the best possible deals and lease advantages.</p>
        </div>
        <div class="faq">
          <h3 class="faq__q">What is the average size of a FLOMBERAY store?</h3>
          <p class="faq__a">The size of a FLOMBERAY store varies according to the location and range of services it provides.<br>Mall Locations (kiosk- island-store) : 220 - 800 sq.ft<br>Street Location (store) : 1200 - 1600 sq.ft<br>Street location (FLOMBERAY MEGA) : 2200 + Sq.ft</p>
        </div>
        <div class="faq">
          <h3 class="faq__q">How long will it take to open a FLOMBERAY dessert bar?</h3>
          <p class="faq__a">It takes approximately 12-16 weeks to build a FLOMBERAY Store once a retail lease has been signed.</p>
        </div>
      </div>

      <div class="brand brand--red" style="left:46px; top:480px;">
        <span class="brand__dot"></span><span class="brand__name">FLOMBERAY</span>
      </div>
      <p class="folio" style="left:46px;">Frequently Asked Questions II Page 21</p>
    </article>

    <article class="page page--right page--red">
      <svg class="waves" viewBox="0 0 384 150" preserveAspectRatio="none" aria-hidden="true">
        <path d="M0 60 C90 30 170 80 250 55 C310 36 350 70 384 60 L384 150 L0 150 Z" fill="#ef5653"/>
        <path d="M0 100 C100 80 200 120 384 95 L384 150 L0 150 Z" fill="#f06360"/>
      </svg>

      <div class="ribbon">
        <svg width="384" height="40" viewBox="0 0 384 40" aria-hidden="true">
          <polygon points="0,0 292,0 280,27 0,27" fill="var(--red-ribbon)"/>
          <polygon points="268,27 280,27 274,36" fill="#9e1820"/>
        </svg>
        <h2 class="ribbon__title" style="left:46px;">What it takes to succeed?</h2>
      </div>

      <div class="page-tab">
        <svg width="17" height="120" viewBox="0 0 17 120" aria-hidden="true"><polygon points="17,0 0,18 0,102 17,120" fill="var(--red-deep)"/></svg>
        <div class="page-tab__num">2<br>2</div>
      </div>

      <div class="content">
        <div class="faq">
          <h3 class="faq__q">Am I required to work in the dessert bar?</h3>
          <p class="faq__a">We believe that it's important for our franchise partner to be part of the store daily operations. From our experience stores that are run and managed by franchise partners are more likely to succeed and produce phenomenal results. However we offer store management services too for franchisees whom have difficulties or constraints.</p>
        </div>
        <div class="faq">
          <h3 class="faq__q">How do I learn to run my dessert bar?</h3>
          <p class="faq__a">FLOMBERAY conducts a broad 4 week training program for all franchise partners. The program will cover aspects such as the operational aspects and product making. More over the program will provide franchise partners with extensive business management knowledge to assist them run a healthy business. The training program will also provide advice on recruitment procedures and various techniques to keep employees motivated.</p>
        </div>
        <div class="faq">
          <h3 class="faq__q">What happens once my dessert bar opens?</h3>
          <p class="faq__a">Our FLOMBERAY support team will always be there to help with various operational and marketing aspects and will be conducting visits to the store to ensure that franchise partners are on the right track towards success. Furthermore periodical training will be provided to franchise partners to ensure that any new services and products are well understood.</p>
        </div>
      </div>

      <div class="brand brand--white" style="right:20px; top:480px;">
        <span class="brand__dot"></span><span class="brand__name">FLOMBERAY</span>
      </div>
      <p class="folio" style="right:20px;">What it takes to succeed? II Page22</p>
    </article>
  </section>

  <section class="spread spread--photo">
    <div class="photo" role="img" aria-label="Photo of a child eating frozen yogurt from a cup at a table, blurred mall interior behind"></div>

    <svg class="waves" style="height:200px;" viewBox="0 0 767 200" preserveAspectRatio="none" aria-hidden="true">
      <path d="M0 40 C60 90 90 150 200 160 C320 170 420 150 767 165 L767 200 L0 200 Z" fill="rgba(240,120,118,0.55)"/>
      <path d="M0 110 C150 140 300 120 767 150 L767 200 L0 200 Z" fill="rgba(243,163,160,0.5)"/>
    </svg>

    <div class="slogan-box">
      <p class="lead">This phrases can be used in large font as found in the<br><br>MESA CRULLO FRANCHISE KIT .</p>
      <p class="headline">Simply the Best Dessert Place Ever</p>
      <p class="slogan">“Unleash Happiness”</p>
      <p class="slogan">“A place for everyone “</p>
      <p class="slogan">“HEALTHY AND TASTY CAN MIX”</p>
      <p class="slogan">“FULL OF SURPRISES”</p>
      <p class="slogan">“We take pride in making others happy”</p>
      <p class="slogan">“positive personality is a must for our brand to prosper”</p>
    </div>

    <div class="photo-tab photo-tab--left">
      <svg width="17" height="120" viewBox="0 0 17 120" aria-hidden="true"><polygon points="0,0 17,18 17,102 0,120" fill="var(--red)"/></svg>
      <div class="page-tab__num">2<br>3</div>
    </div>
    <div class="photo-tab photo-tab--right">
      <svg width="17" height="120" viewBox="0 0 17 120" aria-hidden="true"><polygon points="17,0 0,18 0,102 17,120" fill="var(--red-deep)"/></svg>
      <div class="page-tab__num">2<br>4</div>
    </div>

    <div class="brand brand--red" style="right:20px; top:478px;">
      <span class="brand__dot"></span><span class="brand__name">FLOMBERAY</span>
    </div>
    <p class="folio" style="left:46px;">II Page23</p>
    <p class="folio" style="right:20px;">II Page24</p>
  </section>

</main>
</body>
</html>
```